Designing a brochures for an educational counseling service provider

We would like a 4 sided design on a 11x8.5 paper, half folded. I have including a sample design we did to give you an idea of what we envision but we welcome creativity to make beautiful looking flyers. Text for the flier is included as well as our logo.
- The most important thing is capturing our audience/market. We will be handing these flies to schools, organizations and individual clients.

www.vormtaleducationalconsultants.com

Target Market(s)

We are targeting international students wanting to study in the U.S and Canada.

Industry/Entity Type

Education

Requirements
Must have
• - Clean and clear
• - Our logo should visible and well placed.
• - Could you the pictures of students, libraries and school buildings or you could use the pictures we already have.
Nice to have
• We would like this to match business cards.

```html
<!DOCTYPE html>
<html lang="en">
<head>
<meta charset="utf-8">
<title>Vormtal International Educational Consultants – Brochure Spread</title>
<link href="https://fonts.googleapis.com/css2?family=Open+Sans:ital,wght@0,400;0,600;0,700;1,400;1,300&family=Titillium+Web:ital,wght@0,600;0,700;1,700&display=swap" rel="stylesheet">
<style>
  :root{
    --stage:#4a4a4a;
    --paper:#ffffff;
    --paper-soft:#f1f2f4;
    --blue:#0a5ea8;
    --blue-deep:#0b3a78;
    --blue-night:#0a2a55;
    --orange:#f07d22;
    --orange-deep:#d9561a;
    --ink:#2d2d2d;
    --cyan:#7fd0ff;
  }
  *{box-sizing:border-box;margin:0;padding:0}
  html,body{width:1200px;height:1200px;overflow:hidden;background:var(--stage)}
  body{font-family:"Open Sans",Arial,sans-serif;color:var(--ink)}
  .spread{position:absolute;left:25px;top:175px;width:1150px;height:850px;display:flex;box-shadow:0 20px 50px rgba(0,0,0,.45)}
  .page{position:relative;width:575px;height:850px;background:var(--paper);overflow:hidden}
  .page--left::after{content:"";position:absolute;right:0;top:0;width:30px;height:100%;background:linear-gradient(90deg,rgba(0,0,0,0),rgba(0,0,0,.12))}
  .page--right::after{content:"";position:absolute;left:0;top:0;width:30px;height:100%;background:linear-gradient(90deg,rgba(0,0,0,.12),rgba(0,0,0,0))}
  .header{position:absolute;left:0;top:0;width:575px;height:90px}
  .header-title{position:absolute;font-family:"Titillium Web",sans-serif;font-weight:700;font-style:italic;color:#fff;font-size:30px;letter-spacing:.5px}
  .header-name{position:absolute;font-family:"Titillium Web",sans-serif;font-weight:600;color:#fff;white-space:nowrap;line-height:1}
  .header-name--about{left:236px;top:58px;font-size:13.5px}
  .header-name--services{left:212px;top:41px;font-size:15px}

  /* left page */
  .student-photo{position:absolute;left:24px;top:92px;width:232px;height:320px;background:radial-gradient(ellipse at 50% 40%,#e9e3df 0%,#d8d3d3 55%,#eef0f2 100%)}
  .about-text{position:absolute;left:270px;top:110px;width:280px;font-size:11px;line-height:15.5px}
  .about-text p+p{margin-top:12px}
  .brand{position:absolute;left:290px;top:405px;display:flex;align-items:center;gap:10px}
  .brand-dot{width:34px;height:34px;border-radius:50%;background:var(--blue)}
  .brand-name{font-family:"Open Sans",sans-serif;font-weight:700;font-size:26px;color:var(--blue-deep);letter-spacing:1px}
  .library-photo{position:absolute;left:0;top:455px;width:575px;height:320px;background:linear-gradient(135deg,#0a2a55 0%,#0c4f9a 45%,#1b78c8 70%,#0a3f80 100%)}
  .quote-box{position:absolute;left:40px;top:560px;width:470px;height:140px;background:rgba(6,22,44,.85);color:#fff;text-align:center;padding:48px 20px 0}
  .quote-mark{position:absolute;left:0;right:0;top:-6px;font-family:Georgia,serif;font-size:80px;font-weight:700;line-height:1}
  .quote-text{font-weight:300;font-style:italic;font-size:19px;line-height:26px}
  .footer{position:absolute;left:0;bottom:0;width:575px;height:100px}
  .footer-url{position:absolute;left:0;right:0;bottom:30px;text-align:center;color:#fff;font-size:15px;letter-spacing:1.5px}

  /* right page */
  .services{position:absolute;left:30px;top:98px;width:520px;font-size:10.2px;line-height:13.5px}
  .intro{font-style:italic}
  .package-title{color:var(--orange-deep);font-weight:700;font-size:10.5px;margin-top:8px}
  .package{list-style:none;margin-left:10px}
  .package li{position:relative;padding-left:10px}
  .package li::before{content:"";position:absolute;left:0;top:5px;width:4px;height:4px;background:var(--orange);border-radius:50%}
  .topic{display:flex;align-items:center;gap:6px;font-weight:700;color:var(--blue-deep);font-size:11px;margin-top:9px}
  .topic-icon{width:10px;height:10px;border-radius:50%;background:#3fa535}
  .services p{margin-top:2px}
  .services p+p{margin-top:6px}
  .services-blue{position:absolute;left:0;top:465px;width:575px;height:310px;background:linear-gradient(160deg,#1770c0 0%,#0d4f98 50%,#0a3270 100%)}
  .services-blue-text{position:absolute;left:30px;top:495px;width:520px;color:#fff;font-size:10.2px;line-height:13.5px}
  .services-blue-text .topic{color:var(--cyan)}
  .services-blue-text .topic-icon{background:var(--cyan)}
  .services-blue-text p+p{margin-top:8px}
</style>
</head>
<body>
<main class="spread">

  <section class="page page--left">
    <svg class="header" viewBox="0 0 575 90" aria-hidden="true">
      <polygon points="0,0 210,0 235,72 0,72" fill="var(--blue)"/>
      <polygon points="205,40 575,40 575,90 222,90" fill="var(--orange)"/>
      <polygon points="0,66 233,66 235,72 0,72" fill="var(--blue-deep)"/>
    </svg>
    <h2 class="header-title" style="left:28px;top:14px">ABOUT US</h2>
    <div class="header-name header-name--about">Vormtal International Educational Consultants, LLC</div>

    <div class="student-photo" role="img" aria-label="Smiling student carrying a backpack and a yellow folder"></div>

    <div class="about-text">
      <p>Our mission is to make quality education accessible and affordable to the families we serve. Our services are designed with the child's future in mind. Whether one is seeking an academic or non-academic environment, it is important to us that we set our clients up for success.</p>
      <p>We are a family-centered organization and our goals are the same as those of our clients, for their child to thrive and reach their goals and dreams. With over 10 years of experience in the business, we are aware of the financial obstacles created by the ever increasing cost in education. Our expert consultants work closely with families to map out their educational budget and find the best affordable and quality educational options.</p>
    </div>

    <div class="brand"><span class="brand-dot"></span><span class="brand-name">VORMTAL</span></div>

    <div class="library-photo" role="img" aria-label="Library interior with bookshelves in blue tones"></div>
    <blockquote class="quote-box">
      <span class="quote-mark">&ldquo;</span>
      <p class="quote-text">We offer comprehensive services to families, students, institutions and governmental organizations.</p>
    </blockquote>

    <svg class="footer" viewBox="0 0 575 100" aria-hidden="true">
      <polygon points="0,20 575,0 575,100 0,100" fill="var(--orange)"/>
      <polygon points="0,20 575,0 575,8 0,28" fill="var(--orange-deep)"/>
    </svg>
    <div class="footer-url">www.vormtaleducationalconsultants.com</div>
  </section>

  <section class="page page--right">
    <svg class="header" viewBox="0 0 575 90" aria-hidden="true">
      <polygon points="0,0 175,0 195,72 0,72" fill="var(--orange)"/>
      <polygon points="180,18 575,18 575,80 200,80" fill="var(--blue-deep)"/>
      <polygon points="0,66 193,66 195,72 0,72" fill="var(--orange-deep)"/>
    </svg>
    <h2 class="header-title" style="left:36px;top:14px">SERVICES</h2>
    <div class="header-name header-name--services">Vormtal International Educational Consultants, LLC</div>

    <div class="services">
      <p class="intro">Finding the right school or program for your child is one of the most important decisions your family will make. The right choice will make a major impact on your child's future.</p>
      <div class="package-title">OUR PACKAGE INCLUDES:</div>
      <ul class="package">
        <li>Intake interview</li>
        <li>Present range of options based on needs and goals of the family</li>
        <li>Interview coaching</li>
        <li>Assistance with application and essays</li>
        <li>Updates on student progress throughout their enrollment with the school</li>
        <li>Advisement on financial documents and visa applications</li>
      </ul>
      <div class="topic"><span class="topic-icon"></span>BOARDING SCHOOLS:</div>
      <p>Students who want the best out of their grade school experience are likely to choose boarding schools because they are proven to better prepare students for university. North American boarding schools provide a quality dynamic experience that will facilitate personal growth in independence, leadership, and confidence as well as provide the academic curriculum necessary to prepare students for university.</p>
      <div class="topic"><span class="topic-icon"></span>COLLEGE ADMISSION:</div>
      <p>As Educational Consultants, we specialize in college/university admissions and we understand how confusing, time-consuming, and stressful the application process can be. Our experienced counselors are here to answer your questions and guide you step by step. As Parents and students may have limited access to information on schools, may not know or understand the entire process as a whole, nor where/how to begin, our expert counselors have a solution.</p>
      <p>Clients increase the odds of admissions with our comprehensive plan of action. We believe that regardless of a student's level of involvement in extra-curricular activities or preparedness, they still possess something they can offer to the university; therefore we help them shine on their college applications.</p>
    </div>

    <div class="services-blue"></div>
    <div class="services-blue-text">
      <div class="topic"><span class="topic-icon"></span>TRANSFER STUDENTS:</div>
      <p>Need to find a school an alternative school that is a better match for you? We work with students and families to transfer from one school to another.</p>
      <div class="topic"><span class="topic-icon"></span>SCHOLARSHIPS:</div>
      <p>Funding the education for your children in some of the world's top schools can be very expensive as tuition and fees increase at an average of 4% every year. We work with you to determine the budget for your family, applying to scholarship available and guide you through the financial aid process.</p>
      <p>Over 70% of our clients have been awarded scholarships or Financial Aid, making your education goals attainable an affordable and your children education possible.</p>
      <p>Our consultants are members of GECA, the leading association for educational consultants in North America.</p>
    </div>

    <svg class="footer" viewBox="0 0 575 100" aria-hidden="true">
      <polygon points="0,0 575,20 575,100 0,100" fill="var(--orange)"/>
      <polygon points="0,0 575,20 575,28 0,8" fill="var(--orange-deep)"/>
    </svg>
    <div class="footer-url">www.vormtaleducationalconsultants.com</div>
  </section>

</main>
</body>
</html>
```